Counseling Practice Business Card

I need a professional looking business card incorporating my new logo that was just completed. Card needs to incorporate my name and title, description of my specialty, my address, my phone number, my fax number, my email and my website URL. I need to be able to choose design on/with different paper colors and textures.
I do not have a lot of business card ideas so I am open to anything but I want bold,sharp, clear card without additional designs other than my logo (see attached file info). I am open to different color backgrounds or paper colors including black. I do not like traditional brackets around area codes in phone number or dashes between numbers in phone number. Am open to other ways of presenting including periods between numbers as appropriate. I do not know enough to know what I like yet but I want card to coordinate and work together with my logo. My practice emphasizes natural mental health interventions so any use of color (with background paper color or the blue and green in my logo) that elicits nature is nice. In addition to black, any natural brown or wood looking background might be desirable also. Most of the offerings so far look very similar and boring.

Target Market(s)

Potential therapy clients and other professionals

Contact Information for Business Card

Card information:
Marcus T. Whitfield, Ph.D.
Licensed Clinical Psychologist
Integrative Health Coach
4812 Ferndale Pkwy NW
Suite 730
Duluth, GA 30096
(770) 555-0142 phone
(770) 555-0186 fax
drmarcuswhitfield@kelvora.com
pathbloomcounseling.com

Font styles to use
Serif
Sans Serif
Other font styles liked:
• anything that you think looks crisp, clear and easily readable

Requirements
Must have
• Any color used should coordinate with my logo design (see attached files).
• Card should be printed horizontally so top and bottom are longest sides of rectangle.
• Background color or paper color should complement and highlight logo. Do not like a white background. black, grey, brown or any color my logo would blend well with.
Nice to have
• I would like designer to utilize color to highlight letters/name or phone-fax-web symbols.
• Bottom edge of card could be highlighted if appropriate to an idea.
Should not have
• I would NOT want the card to have a pure white background at all.
• No clear cards.
• Cards should be oriented with long sides on bottom and top, NOT sides. DO NOT LIKE THIS THIN TALL ORIENTATION.

```html
<!DOCTYPE html>
<html lang="en">
<head>
<meta charset="utf-8">
<title>Pathbloom Counseling – Business Card</title>
<link rel="stylesheet" href="https://fonts.googleapis.com/css2?family=PT+Sans:wght@400;700&display=swap">
<style>
  :root {
    --backdrop: #e9e9e6;
    --card: #f6f4ee;
    --ink: #111111;
    --brand-blue: #3563b0;
    --brand-green: #0e5a2c;
    --band-text: #ffffff;
  }
  * { box-sizing: border-box; margin: 0; padding: 0; }
  html, body {
    width: 1200px;
    height: 740px;
    overflow: hidden;
    background: var(--backdrop);
    font-family: "PT Sans", Arial, sans-serif;
    color: var(--ink);
  }
  .business-card {
    position: absolute;
    left: 100px;
    top: 84px;
    width: 1000px;
    height: 572px;
    background: var(--card);
    box-shadow: 0 14px 36px rgba(0,0,0,0.16);
    overflow: hidden;
  }
  .brand-name {
    position: absolute;
    right: 64px;
    top: 84px;
    display: flex;
    align-items: center;
    gap: 14px;
    font-size: 44px;
    font-weight: 700;
    color: var(--brand-green);
    letter-spacing: 0.5px;
  }
  .brand-dot {
    width: 26px;
    height: 26px;
    border-radius: 50%;
    background: var(--brand-blue);
  }
  .identity {
    position: absolute;
    left: 60px;
    top: 206px;
  }
  .person-name {
    font-size: 33px;
    font-weight: 700;
    line-height: 1.1;
  }
  .person-name .credential { font-weight: 400; }
  .person-title {
    font-size: 24px;
    margin-top: 4px;
  }
  .divider {
    position: absolute;
    left: 60px;
    right: 60px;
    top: 296px;
    height: 2px;
    background: var(--brand-blue);
  }
  .contact {
    position: absolute;
    display: flex;
    flex-direction: column;
    align-items: center;
    gap: 10px;
    font-size: 19px;
    line-height: 1.25;
  }
  .contact-icon {
    width: 44px;
    height: 44px;
    border-radius: 50%;
    background: var(--brand-green);
    display: flex;
    align-items: center;
    justify-content: center;
  }
  .contact-icon svg { width: 24px; height: 24px; fill: #fff; }
  .contact--phone { left: 60px; top: 326px; }
  .contact--email { left: 350px; width: 300px; text-align: center; top: 348px; }
  .contact--address { right: 60px; text-align: center; top: 368px; }
  .web-band {
    position: absolute;
    left: 0; right: 0; bottom: 0;
    height: 84px;
    background: var(--brand-blue);
    display: flex;
    align-items: center;
    justify-content: center;
    color: var(--band-text);
    font-size: 27px;
    letter-spacing: 0.3px;
  }
</style>
</head>
<body>
  <section class="business-card">
    <div class="brand-name"><span class="brand-dot"></span>Pathbloom Counseling</div>

    <div class="identity">
      <h1 class="person-name">Marcus T. Whitfield, <span class="credential">Ph.D.</span></h1>
      <p class="person-title">Licensed Clinical Psychologist/ Integrative Health Coach</p>
    </div>
    <div class="divider"></div>

    <div class="contact contact--phone">
      <span class="contact-icon">
        <svg viewBox="0 0 24 24" aria-hidden="true"><path d="M6.6 10.8a15.2 15.2 0 0 0 6.6 6.6l2.2-2.2a1 1 0 0 1 1-.25 11.4 11.4 0 0 0 3.6.57 1 1 0 0 1 1 1V20a1 1 0 0 1-1 1A17 17 0 0 1 3 4a1 1 0 0 1 1-1h3.5a1 1 0 0 1 1 1c0 1.25.2 2.45.57 3.6a1 1 0 0 1-.25 1z"/></svg>
      </span>
      <p>(770) 555-0142 phone<br>(770) 555-0186 fax</p>
    </div>

    <div class="contact contact--email">
      <span class="contact-icon">
        <svg viewBox="0 0 24 24" aria-hidden="true"><path d="M3 5h18a1 1 0 0 1 1 1v12a1 1 0 0 1-1 1H3a1 1 0 0 1-1-1V6a1 1 0 0 1 1-1zm1 2.2V17h16V7.2l-8 5.6zM5.3 7 12 11.7 18.7 7z"/></svg>
      </span>
      <p>drmarcuswhitfield@kelvora.com</p>
    </div>

    <div class="contact contact--address">
      <span class="contact-icon">
        <svg viewBox="0 0 24 24" aria-hidden="true"><path d="M12 2a7 7 0 0 0-7 7c0 5.2 7 13 7 13s7-7.8 7-13a7 7 0 0 0-7-7zm0 9.5A2.5 2.5 0 1 1 12 6.5a2.5 2.5 0 0 1 0 5z"/></svg>
      </span>
      <p>4812 Ferndale Pkwy NW,<br>Suite 730 Duluth, GA 30096</p>
    </div>

    <div class="web-band">www.pathbloomcounseling.com</div>
  </section>
</body>
</html>
```